Website for Private Psychologist

DO NOT CONTACT ME PRIVATELY

I am a Psychologist offering psychotherapy for individuals and couples, and clinical consultation and training and education for mental and medical health professionals and agencies.

I need a redesign of my website

5 Pages (content is attached for each page)
Home
Jungian Psychotherapy
Clinical Consultation & Professional Development
Curriculum Vitae & Publications
Practice Policies and Forms

Designs can be based on these style websites
https://lqmindcare.info; https://pdtarn.org/; https://dorabellcroftcounselling.com/

Design Concepts
Minimalist Layout: Clean and uncluttered layout with generous white space, allowing the content and visuals to stand out'

Keep a linear, uncluttered, professional design.

Please use only royalty free images and google fonts. Please provide links to any stock images used to verify license.

Target Market(s)

private individual or couples seeking psychotherapy

Industry/Entity Type

Psychotherapy

Number of Pages Required

5+ page

Requirements
Should not have
• No search feature

```html
<!DOCTYPE html>
<html lang="en">
<head>
<meta charset="utf-8">
<title>Julian Marlowe — Doctor of Psychology</title>
<link href="https://fonts.googleapis.com/css2?family=Roboto+Slab:wght@400;500&family=Roboto:wght@400;500;700&display=swap" rel="stylesheet">
<style>
:root{
  --ink:#111111;
  --text:#444444;
  --muted:#777777;
  --rule:#bdbdbd;
  --band:#f2f2f2;
  --white:#ffffff;
  --dark:#2b2b2b;
  --footer-text:#a8a8a8;
  --disc:#e6e6e6;
}
*{box-sizing:border-box;margin:0;padding:0}
html,body{width:1200px;height:3177px;overflow:hidden}
body{position:relative;background:var(--white);font-family:'Roboto',sans-serif;color:var(--text)}
.abs{position:absolute}
.brand{position:absolute;border-left:3px solid var(--ink);padding-left:11px}
.brand-name{font-family:'Roboto Slab',serif;font-size:19px;font-weight:500;color:var(--ink);line-height:22px;white-space:nowrap}
.brand-role{font-size:9px;letter-spacing:.3px;color:var(--muted);text-transform:uppercase;line-height:12px}
.brand.light{border-color:var(--white)}
.brand.light .brand-name{color:var(--white)}
.brand.light .brand-role{color:var(--footer-text)}

/* hero */
.hero{position:absolute;left:0;top:0;width:1200px;height:543px;background:linear-gradient(180deg,#dcdcdc 0%,#ffffff 22%,#ffffff 78%,#d9d9d9 100%)}
.hero-art{position:absolute;left:615px;top:0;width:585px;height:543px;background:linear-gradient(90deg,#3a3a3a 0%,#555555 45%,#2a2a2a 100%)}
.hero-phone{left:760px;top:36px;font-size:12px;color:#eeeeee;display:flex;align-items:center;gap:8px;font-family:'Roboto Slab',serif;white-space:nowrap}
.hero-phone b{color:var(--white);font-family:'Roboto',sans-serif;font-weight:500}
.menu{left:1053px;top:33px}
.hero h1{left:100px;top:187px;width:520px;font-family:'Roboto Slab',serif;font-weight:400;font-size:31px;line-height:38px;color:var(--ink);white-space:nowrap}
.hero-sub{left:100px;top:325px;width:380px;font-size:13px;line-height:21px;color:#222}
.btn{left:100px;top:399px;width:243px;height:47px;background:var(--ink);color:var(--white);font-family:'Roboto Slab',serif;font-size:17px;display:flex;align-items:center;justify-content:center}

/* shared section heads */
.eyebrow{font-family:'Roboto Slab',serif;font-size:14px;letter-spacing:4.5px;color:#333;text-transform:uppercase;white-space:nowrap}
.rule{height:1px;background:var(--rule)}
.h2{font-family:'Roboto Slab',serif;font-weight:400;font-size:23px;line-height:33px;color:var(--ink);white-space:nowrap}
.body{font-size:13px;line-height:21.7px;color:var(--text)}

/* about */
.portrait{left:237px;top:639px;width:312px;height:414px;background:linear-gradient(160deg,#6e6259 0%,#3b3430 45%,#111 100%)}
.call{left:618px;top:1015px;border-left:3px solid var(--ink);padding-left:13px}
.call small{display:flex;align-items:center;gap:6px;font-size:11px;color:#333;font-family:'Roboto Slab',serif}
.call strong{display:block;font-family:'Roboto Slab',serif;font-weight:500;font-size:18px;color:var(--ink);margin-top:3px}

/* services */
.band{left:9px;top:1163px;width:1191px;height:659px;background:var(--band)}
.arch{left:699px;top:1163px;width:192px;height:225px;border-radius:0 0 96px 96px;background:radial-gradient(circle at 45% 55%,#6b6274 0%,#8f9bb0 45%,#c7d0dc 100%)}
.badge{left:860px;top:1236px;width:106px;height:106px;border-radius:50%;background:#4a4a4a;color:var(--white);font-family:'Roboto Slab',serif;font-size:14px;letter-spacing:2.5px;font-weight:500;line-height:20px;text-align:center;display:flex;align-items:center;justify-content:center}
.card{top:1443px;width:227px;height:256px;background:var(--white);padding:22px 28px}
.card h3{font-family:'Roboto Slab',serif;font-weight:400;font-size:13px;letter-spacing:1.2px;color:#333;margin-top:10px;text-transform:uppercase;white-space:nowrap}
.card p{font-size:13px;line-height:21.7px;color:var(--text);margin-top:18px}
.card .arrow{margin-top:12px}

/* experience */
.exp-art{left:0;top:1822px;width:1200px;height:463px;background:linear-gradient(90deg,#a35d55 0%,#9a8bb5 18%,#b4b4b4 35%,#cfcfcf 60%,#bdbdbd 100%)}
.exp-box{left:462px;top:1978px;width:504px;height:307px;background:var(--white)}

/* schedule */
.cal-title{left:592px;top:2424px;font-size:12px;font-weight:700;color:var(--ink)}
.cal-month{left:592px;top:2452px;font-size:11px;color:#333}
.cal-grid{left:589px;top:2486px;display:grid;grid-template-columns:repeat(7,33.4px);grid-auto-rows:30px;font-size:9px;color:#444;text-align:center;align-items:center;justify-items:center}
.cal-grid .hd{font-size:9px;color:#333}
.cal-grid .on{width:22px;height:22px;border-radius:50%;background:var(--disc);display:flex;align-items:center;justify-content:center}
.cal-grid .sel{background:var(--ink);color:var(--white)}
.slots-day{left:847px;top:2452px;font-size:11px;color:#333}
.slot{left:847px;width:119px;height:24px;border:1px solid #999;font-size:11px;color:#222;display:flex;align-items:center;justify-content:center}
.slot.active{background:var(--ink);color:var(--white);border-color:var(--ink)}
.tz{left:594px;top:2714px;font-size:11px;color:#333;display:flex;align-items:center;gap:5px;white-space:nowrap}

/* footer */
.footer{left:0;top:2845px;width:1200px;height:332px;background:var(--dark)}
.social{top:3023px;width:22px;height:22px;border-radius:50%;border:1px solid #777}
.copy{left:100px;top:3087px;font-size:12px;color:var(--footer-text)}
.foot-links{left:481px;top:2942px;list-style:none}
.foot-links li{font-size:12px;color:var(--footer-text);font-family:'Roboto Slab',serif;height:37px;white-space:nowrap}
.contact-h{left:867px;top:2942px;font-family:'Roboto Slab',serif;font-size:16px;color:#e6e6e6}
.contact-row{left:867px;font-size:12px;color:var(--footer-text);display:flex;align-items:center;gap:9px}
.contact-row i{width:22px;height:22px;border-radius:50%;border:1px solid #777;display:flex;align-items:center;justify-content:center}
</style>
</head>
<body>

<!-- Hero -->
<section class="hero">
  <div class="hero-art" role="img" aria-label="Photo of layered grey and black paper head shapes"></div>
  <div class="brand" style="left:100px;top:33px"><div class="brand-name">Julian Marlowe</div><div class="brand-role">Doctor of Psychology</div></div>
  <div class="abs hero-phone">
    <svg width="12" height="12" viewBox="0 0 24 24"><path fill="#eee" d="M6.6 10.8a15 15 0 0 0 6.6 6.6l2.2-2.2c.3-.3.7-.4 1-.2 1.1.4 2.3.6 3.6.6.6 0 1 .4 1 1V20c0 .6-.4 1-1 1A17 17 0 0 1 3 4c0-.6.4-1 1-1h3.5c.6 0 1 .4 1 1 0 1.3.2 2.5.6 3.6.1.3 0 .7-.2 1z"/></svg>
    Call for a consultation: <b>(415) 555-0182</b>
  </div>
  <svg class="abs menu" width="42" height="24" viewBox="0 0 42 24"><path d="M0 1h42M8 12h34M16 23h26" stroke="#fff" stroke-width="2"/></svg>
  <h1 class="abs">Discover Healing and Growth<br>through Jungian Psychotherapy<br>&amp; Consultation</h1>
  <p class="abs hero-sub">Embrace Your Inner Journey with a California Licensed<br>Psychologist in San Francisco</p>
  <a class="abs btn">Book an Appointment</a>
</section>

<!-- About -->
<section>
  <div class="abs portrait" role="img" aria-label="Portrait photo of the psychologist"></div>
  <div class="abs rule" style="left:561px;top:697px;width:85px"></div>
  <div class="abs eyebrow" style="left:656px;top:688px">About</div>
  <h2 class="abs h2" style="left:615px;top:716px">Empowering Transformation<br>through Jungian Psychotherapy</h2>
  <p class="abs body" style="left:618px;top:810px;width:362px">Unlock the potential of your mind and explore the depths of your psyche with our expert Jungian psychotherapy services. As a California Licensed Psychologist, I offer personalized and compassionate therapy for individuals and couples seeking healing and growth. Utilizing Jung's profound insights, we delve into your unconscious, dreams, and archetypes to bring profound insights and facilitate positive changes in your life.</p>
  <div class="abs call">
    <small><svg width="11" height="11" viewBox="0 0 24 24"><path fill="#111" d="M6.6 10.8a15 15 0 0 0 6.6 6.6l2.2-2.2c.3-.3.7-.4 1-.2 1.1.4 2.3.6 3.6.6.6 0 1 .4 1 1V20c0 .6-.4 1-1 1A17 17 0 0 1 3 4c0-.6.4-1 1-1h3.5c.6 0 1 .4 1 1 0 1.3.2 2.5.6 3.6.1.3 0 .7-.2 1z"/></svg>Call for a consultation:</small>
    <strong>(415) 555-0182</strong>
  </div>
</section>

<!-- Services -->
<section>
  <div class="abs band"></div>
  <div class="abs arch" role="img" aria-label="Illustration of a head made of puzzle pieces"></div>
  <div class="abs badge">MENTAL<br>HEALTH</div>
  <div class="abs rule" style="left:0;top:1262px;width:250px"></div>
  <div class="abs eyebrow" style="left:264px;top:1254px">Services</div>
  <h2 class="abs h2" style="left:236px;top:1285px">Professional Clinical Consultation<br>and Training</h2>
  <p class="abs body" style="left:238px;top:1375px;width:400px">Unlock the potential of your mind and explore the depths of your<br>psyche with our expert Jungian psychotherapy services.</p>

  <article class="abs card" style="left:236px">
    <svg width="48" height="48" viewBox="0 0 48 48" fill="none" stroke="#222" stroke-width="1.4"><path d="M23 6c-4-3-10 0-10 4-5 0-7 5-5 8-4 3-3 9 1 11-1 5 4 9 8 8 2 4 6 4 6 1zM25 6c4-3 10 0 10 4 5 0 7 5 5 8 4 3 3 9-1 11 1 5-4 9-8 8-2 4-6 4-6 1z"/><path d="M24 6v32"/></svg>
    <h3>Mindful Insights</h3>
    <p>Harness the power of mindfulness for profound self-discovery and personal growth.</p>
    <svg class="arrow" width="26" height="14" viewBox="0 0 26 14" fill="none" stroke="#222"><circle cx="18" cy="7" r="6" stroke="#ccc"/><path d="M1 7h21M18 4l4 3-4 3"/></svg>
  </article>
  <article class="abs card" style="left:487px">
    <svg width="54" height="44" viewBox="0 0 54 44" fill="none" stroke="#222" stroke-width="1.4"><path d="M27 40 8 22C1 15 5 4 14 4c6 0 10 4 13 8 3-4 7-8 13-8 9 0 13 11 6 18z"/><path d="M20 24h8v-5a3 3 0 1 1 5 0v5h6"/></svg>
    <h3>Relationship Renew</h3>
    <p>Strengthen your connections and cultivate healthy relationships with expert guidance.</p>
    <svg class="arrow" width="26" height="14" viewBox="0 0 26 14" fill="none" stroke="#222"><circle cx="18" cy="7" r="6" stroke="#ccc"/><path d="M1 7h21M18 4l4 3-4 3"/></svg>
  </article>
  <article class="abs card" style="left:739px">
    <svg width="54" height="44" viewBox="0 0 54 44" fill="none" stroke="#222" stroke-width="1.4"><path d="M4 42h14v-8h12v-8h12"/><circle cx="12" cy="12" r="3"/><path d="M12 15v12l-4 8M12 22l6-4M30 6l8 6-8 6M22 12h16"/></svg>
    <h3>Resilience Boost</h3>
    <p>Develop inner strength and resilience to overcome life's challenges with resilience-focused support.</p>
    <svg class="arrow" width="26" height="14" viewBox="0 0 26 14" fill="none" stroke="#222"><circle cx="18" cy="7" r="6" stroke="#ccc"/><path d="M1 7h21M18 4l4 3-4 3"/></svg>
  </article>
</section>

<!-- Experience -->
<section>
  <div class="abs exp-art" role="img" aria-label="Photo of hands forming a heart around a colourful paper head, on crumpled grey paper"></div>
  <div class="abs exp-box"></div>
  <div class="abs rule" style="left:462px;top:2025px;width:63px"></div>
  <div class="abs eyebrow" style="left:539px;top:2017px">Experience</div>
  <h2 class="abs h2" style="left:515px;top:2046px">Education for Mental and Medical<br>Health Professionals</h2>
  <p class="abs body" style="left:515px;top:2142px;width:392px">In the ever-evolving landscape of mental and medical health, ongoing education is essential. Through our educational programs, stay updated with the latest advancements and best practices in the field of Jungian psychotherapy. From workshops to seminars, we offer comprehensive training opportunities to expand your knowledge and excel in your career.</p>
  <div class="abs" style="left:462px;top:2315px;width:504px;height:1px;background:#999"></div>
</section>

<!-- Schedule -->
<section>
  <div class="abs rule" style="left:0;top:2427px;width:258px"></div>
  <div class="abs eyebrow" style="left:272px;top:2419px">Schedule a Call</div>
  <h2 class="abs h2" style="left:238px;top:2448px">Telehealth Convenience</h2>
  <p class="abs body" style="left:238px;top:2508px;width:285px">In today's fast-paced world, accessing mental health services should be easy and flexible. That's why all our appointments are currently available via telehealth. Embrace the convenience of virtual sessions, where you can engage in therapy or consultations from the comfort of your own space, while still receiving the same high-quality care.</p>

  <div class="abs cal-title">Select a Date &amp; Time</div>
  <div class="abs cal-month">July 2023</div>
  <svg class="abs" style="left:780px;top:2454px" width="40" height="14" viewBox="0 0 40 14" fill="none" stroke="#222" stroke-width="1.5"><path d="M8 2 3 7l5 5M30 2l5 5-5 5"/></svg>
  <div class="abs cal-grid">
    <span class="hd">SUN</span><span class="hd">MON</span><span class="hd">TUE</span><span class="hd">WED</span><span class="hd">THU</span><span class="hd">FRI</span><span class="hd">SAT</span>
    <span></span><span></span><span></span><span></span><span></span><span></span><span>1</span>
    <span>2</span><span>3</span><span>4</span><span>5</span><span>6</span><span>7</span><span>8</span>
    <span>9</span><span>10</span><span>11</span><span>12</span><span>13</span><span>14</span><span>15</span>
    <span>16</span><span>17</span><span>18</span><span>19</span><span>20</span><span>21</span><span class="on">22</span>
    <span class="on sel">23</span><span class="on">24</span><span class="on">25</span><span class="on">26</span><span class="on">27</span><span class="on">28</span><span class="on">29</span>
    <span class="on">30</span><span class="on">31</span>
  </div>
  <div class="abs slots-day">Monday, July 23</div>
  <div class="abs slot" style="top:2491px">10:30 am</div>
  <div class="abs slot active" style="top:2522px">11:00 am</div>
  <div class="abs slot" style="top:2553px">11:30 am</div>
  <div class="abs tz"><svg width="14" height="14" viewBox="0 0 24 24" fill="none" stroke="#222" stroke-width="2"><circle cx="12" cy="12" r="10"/><path d="M2 12h20M12 2a15 15 0 0 1 0 20M12 2a15 15 0 0 0 0 20"/></svg>Eastern time - Us California (03: 32 pm) <span style="font-size:8px">▼</span></div>
</section>

<!-- Footer -->
<footer>
  <div class="abs footer"></div>
  <div class="brand light" style="left:100px;top:2955px"><div class="brand-name">Julian Marlowe</div><div class="brand-role">Doctor of Psychology</div></div>
  <span class="abs social" style="left:100px"></span>
  <span class="abs social" style="left:134px"></span>
  <span class="abs social" style="left:167px"></span>
  <span class="abs social" style="left:200px"></span>
  <div class="abs copy">© Julian Marlowe 2023</div>
  <ul class="abs foot-links">
    <li>Home</li>
    <li>Jungian Psychotherapy</li>
    <li>Clinical Consultation &amp; Professional Development</li>
    <li>Curriculum Vitae &amp; Publications</li>
    <li>Practice Policies and Forms</li>
  </ul>
  <div class="abs contact-h">Contact</div>
  <div class="abs contact-row" style="top:2981px"><i><svg width="10" height="10" viewBox="0 0 24 24"><path fill="#bbb" d="M6.6 10.8a15 15 0 0 0 6.6 6.6l2.2-2.2c.3-.3.7-.4 1-.2 1.1.4 2.3.6 3.6.6.6 0 1 .4 1 1V20c0 .6-.4 1-1 1A17 17 0 0 1 3 4c0-.6.4-1 1-1h3.5c.6 0 1 .4 1 1 0 1.3.2 2.5.6 3.6.1.3 0 .7-.2 1z"/></svg></i>(415) 555-0182</div>
  <div class="abs contact-row" style="top:3018px"><i><svg width="10" height="10" viewBox="0 0 24 24"><path fill="#bbb" d="M2 5h20v14H2z"/><path d="m2 5 10 8 10-8" stroke="#2b2b2b" stroke-width="2" fill="none"/></svg></i>jmarlowe@mailbox.net</div>
</footer>

</body>
</html>
```